K & R Ground Works. Business card design

We need a business card designed for a new business. We have a bulldozer and tractor service. We clear land and make wildlife food plots. We provide disking, bush hogging, and site prep services.
I have attached an image of a business card that I like and would like my business cards to look similar.

Target Market(s)

anyone needing bulldozer and/or tractor services

Industry/Entity Type

Business

Contact Information for Business Card

K & R Ground Works, Operated by 7-T-Ranch
Dale Whitcomb
601-555-0148
dwk4821@mailbarn.example

Font styles to use
Sans Serif

Colors

Designer to choose colors to be used in the design.

Requirements
Must have
• image of tractor and bulldozer
• Land Clearing
• Wildlife food plots
• Bush Hogging
• Disking
• Site prep
Nice to have
• i have included a image of a business card that i like. I would like mine to be similar.

```html
<!DOCTYPE html>
<html lang="en">
<head>
<meta charset="utf-8">
<title>K &amp; R Ground Works – Business Card</title>
<link rel="stylesheet" href="https://fonts.googleapis.com/css2?family=Oswald:wght@300;400;500&family=Roboto+Condensed:wght@400&display=swap">
<style>
  :root {
    --stage: #e9e6e1;
    --card-black: #0b0b0b;
    --accent-red: #e2483f;
    --text-white: #ffffff;
    --leaf-dark: #2f4a22;
    --leaf-mid: #4f7a34;
    --leaf-light: #8fb06a;
    --sky: #b9cfc9;
  }
  * { margin: 0; padding: 0; box-sizing: border-box; }
  html, body {
    width: 1200px; height: 1023px; overflow: hidden;
    background: var(--stage);
  }
  .business-card {
    position: absolute; left: 100px; top: 226px;
    width: 1000px; height: 572px;
    background: var(--card-black);
    overflow: hidden;
    box-shadow: 0 14px 40px rgba(0,0,0,.25);
  }
  .equipment-photo {
    position: absolute; inset: 0;
    background:
      radial-gradient(ellipse 30% 40% at 38% 42%, rgba(200,170,40,.45), transparent 70%),
      linear-gradient(180deg, var(--sky) 0%, var(--leaf-light) 18%, var(--leaf-mid) 45%, var(--leaf-dark) 100%);
  }
  .photo-fade {
    position: absolute; inset: 0;
    background:
      linear-gradient(90deg, transparent 0%, rgba(0,0,0,.15) 30%, rgba(0,0,0,.85) 55%, var(--card-black) 64%),
      linear-gradient(180deg, transparent 45%, rgba(0,0,0,.8) 78%, var(--card-black) 100%);
  }
  .brand-block {
    position: absolute; left: 190px; top: 262px;
    width: 460px;
  }
  .brand-name {
    font-family: "Oswald", sans-serif; font-weight: 400;
    font-size: 46px; line-height: 1; color: var(--text-white);
    letter-spacing: 1px; text-transform: uppercase;
    white-space: nowrap;
  }
  .brand-operator {
    margin-top: 8px; padding-left: 14px;
    font-family: "Oswald", sans-serif; font-weight: 300;
    font-size: 22px; line-height: 1; color: var(--accent-red);
    letter-spacing: 6px; text-transform: uppercase;
    white-space: nowrap;
  }
  .contact-frame {
    position: absolute; left: 176px; top: 390px;
    width: 440px; height: 152px;
    border: 2px solid var(--accent-red);
    padding: 14px 20px;
  }
  .contact-name {
    font-family: "Oswald", sans-serif; font-weight: 500;
    font-size: 44px; line-height: 1; color: var(--accent-red);
    text-transform: uppercase; letter-spacing: 1px;
    white-space: nowrap;
  }
  .contact-line {
    display: flex; align-items: center; gap: 12px; margin-top: 10px;
    font-family: "Roboto Condensed", sans-serif;
    font-size: 24px; line-height: 1; color: var(--text-white);
    white-space: nowrap;
  }
  .contact-line svg { width: 16px; height: 16px; flex: none; }
  .services-frame {
    position: absolute; left: 680px; top: 34px;
    width: 290px; height: 330px;
    border: 2px solid var(--accent-red);
    display: flex; flex-direction: column; justify-content: center;
    padding-left: 28px;
  }
  .services-list { list-style: none; }
  .services-list li {
    font-family: "Oswald", sans-serif; font-weight: 400;
    font-size: 28px; line-height: 1.35; color: var(--text-white);
    text-transform: uppercase; white-space: nowrap;
  }
</style>
</head>
<body>
  <section class="business-card">
    <div class="equipment-photo" role="img" aria-label="Photo of a bulldozer and tractor among green trees"></div>
    <div class="photo-fade"></div>

    <div class="brand-block">
      <h1 class="brand-name">K &amp; R Ground Works</h1>
      <p class="brand-operator">Operated by 7-T-Ranch</p>
    </div>

    <div class="contact-frame">
      <p class="contact-name">Dale Whitcomb</p>
      <p class="contact-line">
        <svg viewBox="0 0 16 16" aria-hidden="true"><path d="M4 1.5 6 5 4.6 6.4c.8 1.8 2.2 3.2 4 4L10 9l3.5 2-1 2.8C7 13.5 2.5 9 2.2 3.5z" fill="none" stroke="var(--accent-red)" stroke-width="1.5"/></svg>
        601-555-0148
      </p>
      <p class="contact-line">
        <svg viewBox="0 0 16 16" aria-hidden="true"><rect x="1.5" y="3" width="13" height="10" fill="none" stroke="var(--accent-red)" stroke-width="1.5"/><path d="M1.5 3 8 9l6.5-6" fill="none" stroke="var(--accent-red)" stroke-width="1.5"/></svg>
        dwk4821@mailbarn.example
      </p>
    </div>

    <div class="services-frame">
      <ul class="services-list">
        <li>Land Clearing</li>
        <li>Wildlife Food Plots</li>
        <li>Bush Hogging</li>
        <li>Disking – Site Prep</li>
      </ul>
    </div>
  </section>
</body>
</html>
```